Dorsey K. Wendell Business Card

We need a business card for our company Dorsey K. Wendell Heating & Plumbing to be distributed to potential customers. It should follow the color scheme of our logo and have a modern upscale and masculine look.

The logo is attached and the info below should also be included:

5187 W. Cedar Brook Rd.
Ashford, PA 17388

Russell T. Wendell
(717) 592-0817
russelltwendell@fernmail.net
dorseykwendell.net
PA #093148

Industry/Entity Type

Business

Contact Information for Business Card

5187 W. Cedar Brook Rd.
Ashford, PA 17388

Russell T. Wendell
(717) 592-0817
russelltwendell@fernmail.net
dorseykwendell.net
PA #093148

Colors

Designer to choose colors to be used in the design.

Requirements
Must have
• Information above included

```html
<!DOCTYPE html>
<html lang="en">
<head>
<meta charset="utf-8">
<title>Dorsey K. Wendell Business Card</title>
<link rel="stylesheet" href="https://fonts.googleapis.com/css2?family=Open+Sans:wght@400;700&display=swap">
<style>
  :root {
    --blue: #2166ad;
    --green-light: #b3d84a;
    --green-dark: #9fc73d;
    --ink: #4a4a4a;
    --white: #ffffff;
    --globe-light: #efefef;
    --globe-dark: #d3d4d6;
    --tab: rgba(255, 255, 255, 0.22);
  }
  html, body {
    margin: 0;
    padding: 0;
    width: 1200px;
    height: 686px;
    overflow: hidden;
    background: var(--white);
  }
  .card {
    position: relative;
    width: 1050px;
    height: 600px;
    transform: scale(1.142857);
    transform-origin: 0 0;
    overflow: hidden;
    background: var(--white);
    font-family: "Open Sans", Arial, sans-serif;
  }
  .card-shapes {
    position: absolute;
    inset: 0;
  }
  .holder-name {
    position: absolute;
    left: 38px;
    top: 88px;
    margin: 0;
    font-size: 58px;
    line-height: 1;
    color: var(--ink);
    font-weight: 400;
    white-space: nowrap;
  }
  .holder-name strong { font-weight: 700; }
  .license {
    position: absolute;
    left: 45px;
    top: 170px;
    margin: 0;
    font-size: 22px;
    color: var(--ink);
  }
  .contact-list {
    list-style: none;
    margin: 0;
    padding: 0;
  }
  .contact-item {
    position: absolute;
    left: 0;
    height: 44px;
    display: flex;
    align-items: center;
  }
  .contact-tab {
    position: relative;
    width: 82px;
    height: 44px;
    background: var(--tab);
    border-left: 8px solid var(--white);
    box-sizing: border-box;
  }
  .contact-icon {
    position: absolute;
    left: 29px;
    top: 3px;
    width: 38px;
    height: 38px;
    border-radius: 50%;
    background: var(--white);
    display: flex;
    align-items: center;
    justify-content: center;
  }
  .contact-icon svg { width: 20px; height: 20px; }
  .contact-text {
    margin-left: 26px;
    font-size: 25px;
    line-height: 34px;
    color: var(--white);
    white-space: nowrap;
  }
  .item-phone { top: 297px; }
  .item-email { top: 370px; }
  .item-web { top: 441px; }
  .item-address { top: 515px; }
  .item-address .contact-text { margin-top: -8px; }
</style>
</head>
<body>
<div class="card">
  <svg class="card-shapes" viewBox="0 0 1050 600" width="1050" height="600">
    <defs>
      <linearGradient id="globeShade" x1="0" y1="0" x2="1" y2="0">
        <stop offset="0" stop-color="var(--globe-light)"/>
        <stop offset="1" stop-color="var(--globe-dark)"/>
      </linearGradient>
    </defs>
    <circle class="globe" cx="725" cy="335" r="347" fill="url(#globeShade)" role="img" aria-label="Globe with a map of North America"/>
    <polygon class="top-band-green" points="0,0 780,0 815,45 0,45" fill="var(--green-light)"/>
    <polygon class="top-band-green-shade" points="480,0 780,0 815,45 515,45" fill="var(--green-dark)"/>
    <polygon class="top-band-blue" points="780,0 1050,0 1050,122 567,122 515,45 815,45" fill="var(--blue)"/>
    <polygon class="phone-band" points="0,273 285,273 343,353 0,353" fill="var(--green-light)"/>
    <polygon class="contact-band" points="0,353 808,353 977,600 0,600" fill="var(--blue)"/>
    <polygon class="bottom-band-green" points="617,545 940,545 977,600 655,600" fill="var(--green-dark)"/>
    <polygon class="bottom-band-green-light" points="940,545 1050,545 1050,600 977,600" fill="var(--green-light)"/>
  </svg>

  <h1 class="holder-name"><strong>Russell T.</strong> Wendell</h1>
  <p class="license">PA #093148</p>

  <ul class="contact-list">
    <li class="contact-item item-phone">
      <span class="contact-tab"><span class="contact-icon">
        <svg viewBox="0 0 24 24"><path fill="var(--green-light)" d="M6.6 10.8a15.1 15.1 0 0 0 6.6 6.6l2.2-2.2a1 1 0 0 1 1-.25 11.4 11.4 0 0 0 3.6.57 1 1 0 0 1 1 1V20a1 1 0 0 1-1 1A17 17 0 0 1 3 4a1 1 0 0 1 1-1h3.5a1 1 0 0 1 1 1c0 1.25.2 2.45.57 3.570a1 1 0 0 1-.25 1z"/></svg>
      </span></span>
      <span class="contact-text">(717) 592-0817</span>
    </li>
    <li class="contact-item item-email">
      <span class="contact-tab"><span class="contact-icon">
        <svg viewBox="0 0 24 24"><rect x="2" y="5" width="20" height="14" rx="2" fill="var(--blue)"/><path d="M3 6l9 7 9-7" fill="none" stroke="var(--white)" stroke-width="1.6"/></svg>
      </span></span>
      <span class="contact-text">russelltwendell@fernmail.net</span>
    </li>
    <li class="contact-item item-web">
      <span class="contact-tab"><span class="contact-icon">
        <svg viewBox="0 0 24 24"><circle cx="12" cy="12" r="10" fill="var(--blue)"/><path d="M12 2v20M2 12h20M12 2c-4 3-4 17 0 20M12 2c4 3 4 17 0 20" fill="none" stroke="var(--white)" stroke-width="1.2"/></svg>
      </span></span>
      <span class="contact-text">dorseykwendell.net</span>
    </li>
    <li class="contact-item item-address">
      <span class="contact-tab"><span class="contact-icon">
        <svg viewBox="0 0 24 24"><path fill="var(--blue)" d="M12 3l10 9h-3v9h-5v-6h-4v6H5v-9H2z"/></svg>
      </span></span>
      <span class="contact-text">5187 W. Cedar Brook Rd.<br>Ashford, PA 17388</span>
    </li>
  </ul>
</div>
</body>
</html>
```